Kit Darvell - health and fitness coach who needs a web page. simple and effective

I am a online health and fitness coach who runs a 10 week challenge 4 times a year. I am wanting, a menu with a bit about me, a place where people can buy the programme, testimonies, memberships, photos, and recipes.
I am wanting it to look modern, professional and simple.
The website is how potential clients can check out the memberships for the programme, photos of myself and and my family to show members that I am a confident, educated, independent and healthy woman. Who is very passionate about making a difference in people lives to become a better version of themselves.
My training philosophy is simple, Commitment to training, Consistently working hard and training equals Change! Change is physical changes to the body!!

Target Market(s)

Woman 25-44 years

Industry/Entity Type

Health And Wellness

Coding

Coded - Design and coding required

Number of Pages Required

5+ page

Font styles to use
Sans Serif

Colors
fbed22
e667a6
ffffff

Requirements
Must have
• I like the style of "plain tile" website design.
• On the menu bar I want 9 different tabs/options to click on, these are named:
• BLOG
• ABOUT
• TRAINING PROGRAMS
• HEALTHY FOOD
• SUBSCRIBE
• TESTIMONIALS
• CHATWALL
• SNAPLOOMER
• VID REEL
Nice to have
• logo at the top (attached under file 2)
• Easy for myself to add information once website design is completed.
• lots of white space, white a bright yellow (same as logo) or pink
Should not have
• clutter

```html
<!DOCTYPE html>
<html lang="en">
<head>
<meta charset="utf-8">
<title>Kit Darvell – Online Health and Fitness Coaching</title>
<link href="https://fonts.googleapis.com/css2?family=Lato:wght@300;400;700;900&display=swap" rel="stylesheet">
<style>
:root{
  --yellow:#fbed22;
  --yellow-deep:#f2c70f;
  --pink:#e667a6;
  --pink-deep:#d9468f;
  --white:#ffffff;
  --ink:#2b2b2b;
  --text:#555555;
  --line:#e2e2e2;
  --grey:#e9e9e9;
  --grey-light:#f3f3f3;
}
*{box-sizing:border-box;margin:0;padding:0}
html,body{width:1200px;height:4878px;overflow:hidden}
body{position:relative;background:var(--white);font-family:'Lato',sans-serif;color:var(--text)}
section,header,footer{position:absolute;left:0;width:1200px}
.photo{position:absolute}
a{color:inherit;text-decoration:none}

/* header */
.site-header{top:0;height:104px;background:var(--white)}
.brand{position:absolute;display:flex;align-items:center;gap:12px}
.brand-dot{width:22px;height:22px;border-radius:50%;background:var(--pink)}
.brand-name{font-size:24px;line-height:28px;font-weight:700;color:var(--ink);white-space:nowrap}
.site-header .brand{left:114px;top:36px}
.social-top{position:absolute;right:112px;top:16px;display:flex;gap:20px;font-size:11px;color:var(--ink);list-style:none}
.social-top li,.footer-col li.social{display:flex;align-items:center;gap:6px}
.dot-icon{width:9px;height:9px;border-radius:50%;background:var(--pink);display:inline-block}
.main-nav{position:absolute;right:112px;top:56px;display:flex;gap:18px;font-size:13px;color:var(--ink);list-style:none}
.main-nav li.current{font-weight:700;border-bottom:2px solid var(--ink);padding-bottom:3px}

/* hero */
.hero{top:104px;height:626px;background:linear-gradient(115deg,var(--yellow) 0%,var(--yellow) 30%,#f4ae4e 55%,#ec7f8c 75%,var(--pink) 100%)}
.hero-ring{position:absolute;left:120px;top:60px;width:440px;height:440px;border-radius:50%;background:var(--white);box-shadow:0 6px 20px rgba(0,0,0,.12)}
.hero-photo{position:absolute;left:20px;top:20px;width:400px;height:400px;border-radius:50%;background:radial-gradient(circle at 45% 40%,#c9c3bd,#8d8a86 60%,#5e5c5a)}
.hero-title{position:absolute;left:602px;top:168px;font-size:42px;line-height:52px;font-weight:700;color:var(--white)}
.hero-sub{position:absolute;left:602px;top:282px;width:420px;font-size:17px;line-height:24px;color:var(--white)}
.btn{position:absolute;display:flex;align-items:center;justify-content:center;font-size:14px;font-weight:700;letter-spacing:.5px}
.btn-hero{left:602px;top:361px;width:162px;height:44px;background:var(--white);color:var(--pink-deep)}
.slider-dots{position:absolute;display:flex;align-items:center;gap:8px}
.slider-dots span{width:9px;height:9px;border-radius:50%;background:var(--white)}
.slider-dots span.arrow{width:20px;height:20px;background:var(--ink);display:flex;align-items:center;justify-content:center}
.slider-dots.dark span{background:var(--ink)}
.slider-dots.dark span.empty{background:transparent;border:2px solid var(--ink)}
.drip{position:absolute;left:0;width:1200px}

/* about */
.about{top:730px;height:642px}
.section-title-left{position:absolute;left:124px;top:164px;font-size:32px;line-height:38px;font-weight:400;color:var(--pink)}
.about-text{position:absolute;left:124px;top:255px;width:430px;font-size:16px;line-height:25px;color:var(--text)}
.btn-yellow{left:124px;top:421px;width:168px;height:46px;background:var(--yellow);color:var(--pink-deep)}
.about-photo-back{left:572px;top:83px;width:300px;height:446px;background:linear-gradient(160deg,#e86a98,#f4a3c2 55%,#c65486)}
.about-photo-front{left:667px;top:151px;width:416px;height:312px;border:10px solid var(--white);box-shadow:0 8px 24px rgba(0,0,0,.25);background:linear-gradient(180deg,#9ec3e3 0%,#cfe2f0 45%,#4f8fae 55%,#d8c7a2 75%,#c7b48c 100%)}

/* buy */
.buy{top:1372px;height:504px;background:var(--grey)}
.buy-photo{left:0;top:0;width:605px;height:504px;background:linear-gradient(135deg,#8a7767,#b9a593 45%,#6e8a55 80%,#51683e)}
.buy-card{position:absolute;left:537px;top:78px;width:585px;height:348px;background:var(--white);box-shadow:0 6px 22px rgba(0,0,0,.15)}
.buy-card h2{position:absolute;left:54px;top:50px;font-size:32px;font-weight:400;color:var(--ink);letter-spacing:.5px}
.buy-card p{position:absolute;left:54px;top:108px;width:490px;font-size:15px;line-height:24px;color:var(--text)}
.btn-pink{left:54px;top:267px;width:184px;height:44px;background:var(--pink-deep);color:var(--white);font-size:13px}

/* testimonials */
.testimonials{top:1876px;height:530px;background:var(--yellow)}
.center-title{position:absolute;left:0;width:1200px;text-align:center;font-size:30px;font-weight:400;color:var(--ink);letter-spacing:.5px}
.avatar{position:absolute;left:554px;top:123px;width:92px;height:92px;border-radius:50%;background:linear-gradient(160deg,#b08f73,#6d5747);border:4px solid var(--white)}
.quote{position:absolute;left:280px;top:230px;width:640px;text-align:center;font-size:15px;line-height:24px;color:var(--ink)}
.quote-mark{position:absolute;top:208px;font-size:80px;line-height:80px;font-weight:900;color:var(--ink)}
.author{position:absolute;left:0;width:1200px;top:338px;text-align:center;font-size:14px;font-weight:700;color:var(--ink)}

/* membership */
.membership{top:2406px;height:625px}
.plan{position:absolute;background:var(--white);box-shadow:0 4px 18px rgba(0,0,0,.14);text-align:center}
.plan-head{position:relative;height:88px;display:flex;align-items:flex-start;justify-content:center;padding-top:22px;font-size:22px;font-weight:700;color:var(--ink)}
.plan-head svg{position:absolute;left:0;bottom:0;width:100%;height:30px}
.plan.bronze .plan-head{background:var(--yellow)}
.plan.gold .plan-head{background:var(--yellow-deep)}
.plan.silver .plan-head{background:var(--pink-deep);color:var(--white);font-weight:400;font-size:26px;height:100px}
.plan ul{list-style:none;margin:10px 24px 0}
.plan li{font-size:14px;line-height:39px;color:var(--text);border-bottom:1px solid var(--line)}
.plan li:last-child{border-bottom:none}
.price{font-size:32px;font-weight:400;color:var(--ink);margin-top:14px}
.plan.silver .price{color:var(--pink-deep);font-size:36px}

/* recipes */
.recipes{top:3031px;height:741px;background:var(--pink)}
.recipes .center-title{color:var(--white)}
.recipe-card{position:absolute;background:var(--white);box-shadow:0 4px 14px rgba(0,0,0,.15)}
.recipe-img{position:absolute;left:0;top:0;width:100%}
.recipe-body{position:absolute;left:24px;right:24px}
.recipe-title{font-size:17px;font-weight:700;color:var(--pink-deep)}
.recipe-text{font-size:13px;line-height:18px;color:var(--text);margin-top:4px}
.recipe-card.small .recipe-body{left:22px;right:14px}
.recipe-card.small .recipe-title{font-size:16px}
.recipe-card.small .recipe-text{font-size:11px;line-height:15px}

/* gallery */
.gallery{top:3772px;height:732px;background:linear-gradient(180deg,var(--white) 0%,var(--grey-light) 55%,#e4e4e4 100%)}
.tile{position:absolute;width:234px}

/* footer */
.site-footer{top:4504px;height:374px;background:var(--white)}
.site-footer .brand{left:120px;top:100px}
.footer-col{position:absolute;top:76px}
.footer-col h3{font-size:15px;font-weight:700;color:var(--pink-deep);letter-spacing:.5px;margin-bottom:14px}
.footer-col ul{list-style:none}
.footer-col li{font-size:13px;line-height:33px;color:var(--ink)}
.footer-rule{position:absolute;left:120px;top:309px;width:960px;height:1px;background:var(--line)}
.copyright{position:absolute;left:0;width:1200px;top:330px;text-align:center;font-size:13px;color:var(--text)}
</style>
</head>
<body>

<header class="site-header">
  <div class="brand">
    <span class="brand-dot"></span>
    <span class="brand-name">Kit Darvell</span>
  </div>
  <ul class="social-top">
    <li><span class="dot-icon"></span>CHATWALL</li>
    <li><span class="dot-icon"></span>SNAPLOOMER</li>
    <li><span class="dot-icon"></span>VID REEL</li>
  </ul>
  <ul class="main-nav">
    <li class="current">HOME</li>
    <li>BLOG</li>
    <li>ABOUT</li>
    <li>TRAINING PROGRAMS</li>
    <li>HEALTHY FOOD</li>
    <li>SUBSCRIBE</li>
    <li>TESTIMONIALS</li>
  </ul>
</header>

<section class="hero">
  <div class="hero-ring">
    <div class="hero-photo" role="img" aria-label="Portrait of the coach flexing her arm in a gym"></div>
  </div>
  <h1 class="hero-title">Online Health and<br>Fitness Coaching Services</h1>
  <p class="hero-sub">Morbi diam mauris viverra in gravida eu mattis in<br>ante Morbi eget arcu Morbi porta libero</p>
  <a class="btn btn-hero">START NOW</a>
  <div class="slider-dots" style="left:540px;top:543px">
    <span class="arrow"><svg width="8" height="8" viewBox="0 0 8 8"><path d="M5.5 1 2.5 4 5.5 7" fill="none" stroke="#fff" stroke-width="1.6"/></svg></span>
    <span></span><span></span><span></span><span></span>
    <span class="arrow"><svg width="8" height="8" viewBox="0 0 8 8"><path d="M2.5 1 5.5 4 2.5 7" fill="none" stroke="#fff" stroke-width="1.6"/></svg></span>
  </div>
  <svg class="drip" style="top:566px;height:60px" viewBox="0 0 1200 60" preserveAspectRatio="none">
    <path fill="#ffffff" d="M0 60 V30 C30 20 50 50 80 38 C105 28 120 16 150 24 C180 32 175 52 210 48 C240 44 235 20 270 22 C300 24 300 40 330 38 C360 36 360 16 395 20 C430 24 420 54 460 53 C495 52 480 22 520 21 C560 20 555 38 590 36 C625 34 620 13 660 16 C700 20 690 47 730 46 C770 45 760 22 800 22 C835 22 830 35 865 33 C900 31 895 10 935 12 C975 14 965 50 1005 47 C1040 45 1030 16 1070 14 C1110 12 1110 31 1140 26 C1165 22 1175 3 1200 0 V60 Z"/>
  </svg>
</section>

<section class="about">
  <h2 class="section-title-left">LITTLE ABOUT<br>KIT DARVELL</h2>
  <p class="about-text">Kit Darvell is Coach Kit. A health and fitness coach since 2008 after completing a Bachelor of Recreation and Sports at Ashbury University. She has also obtained other qualifications of National Strength and Conditioning Coach Level 1</p>
  <a class="btn btn-yellow">READ MORE</a>
  <div class="photo about-photo-back" role="img" aria-label="Pink berry smoothie in a glass"></div>
  <div class="photo about-photo-front" role="img" aria-label="Coach doing a handstand on a beach"></div>
</section>

<section class="buy">
  <div class="photo buy-photo" role="img" aria-label="Coach biting into a head of broccoli beside fresh vegetables"></div>
  <div class="buy-card">
    <h2>BUY PROGRAMME</h2>
    <p>Kit's passion and motivation for fitness is infectious, attracting people worldwide who complete her online fitness programs. The sweat &amp; shred fitness challenge is for anyone who wants to improve there fitness and strength. On each workout there are "scaling" options, so you just go at your own pace.</p>
    <a class="btn btn-pink">BUY PROGRAMME</a>
  </div>
</section>

<section class="testimonials">
  <h2 class="center-title" style="top:66px">TESTIMONIALS</h2>
  <div class="avatar" role="img" aria-label="Client portrait"></div>
  <span class="quote-mark" style="left:236px">“</span>
  <p class="quote">Anim in massa libero interdum nec interdum vel blandit sed nulla in ullamcorper est eget tempor cursus neque mi consectetuer mi a ultricies massa est sed nisl Class aptent taciti sociosqu ad litora torquent per conubi</p>
  <span class="quote-mark" style="left:926px">”</span>
  <p class="author">BY AUTHOR NAME</p>
  <div class="slider-dots dark" style="left:540px;top:400px">
    <span class="arrow"><svg width="8" height="8" viewBox="0 0 8 8"><path d="M5.5 1 2.5 4 5.5 7" fill="none" stroke="#fff" stroke-width="1.6"/></svg></span>
    <span></span><span class="empty"></span><span class="empty"></span><span class="empty"></span>
    <span class="arrow"><svg width="8" height="8" viewBox="0 0 8 8"><path d="M2.5 1 5.5 4 2.5 7" fill="none" stroke="#fff" stroke-width="1.6"/></svg></span>
  </div>
  <svg class="drip" style="top:446px;height:84px" viewBox="0 0 1200 84" preserveAspectRatio="none">
    <path fill="#ffffff" d="M0 84 V40 C40 20 60 70 100 60 C140 50 130 14 175 18 C215 22 210 72 250 70 C290 68 280 28 320 30 C360 32 355 66 395 62 C435 58 425 16 470 20 C510 24 505 78 545 74 C585 70 575 30 615 32 C655 34 650 62 690 58 C730 54 720 12 765 16 C805 20 800 70 840 66 C880 62 870 28 910 30 C950 32 945 74 985 70 C1025 66 1015 20 1060 22 C1100 24 1095 60 1135 56 C1170 52 1180 28 1200 24 V84 Z"/>
  </svg>
</section>

<section class="membership">
  <h2 class="center-title" style="top:52px">MEMBERSHIP</h2>
  <div class="plan bronze" style="left:163px;top:163px;width:283px;height:348px">
    <div class="plan-head">BRONZE<svg viewBox="0 0 100 30" preserveAspectRatio="none"><path d="M0 30 V18 C30 0 70 30 100 10 V30 Z" fill="#fff"/></svg></div>
    <ul><li>Praesent elementum elit</li><li>At tellus nec ultricies</li><li>Sit amet porttitor</li><li>Mattis enim in massa</li><li>Libero interdum nec</li></ul>
    <p class="price">$ 25.99</p>
  </div>
  <div class="plan silver" style="left:446px;top:131px;width:321px;height:400px;z-index:2">
    <div class="plan-head">SILVER<svg viewBox="0 0 100 30" preserveAspectRatio="none"><path d="M0 30 V10 C35 34 65 34 100 10 V30 Z" fill="#fff"/></svg></div>
    <ul><li>Praesent elementum elit</li><li>At tellus nec ultricies</li><li>Sit amet porttitor</li><li>Mattis enim in massa</li><li>Libero interdum nec</li></ul>
    <p class="price">$ 49.99</p>
  </div>
  <div class="plan gold" style="left:767px;top:163px;width:283px;height:348px">
    <div class="plan-head">GOLD<svg viewBox="0 0 100 30" preserveAspectRatio="none"><path d="M0 30 V10 C30 30 70 0 100 18 V30 Z" fill="#fff"/></svg></div>
    <ul><li>Praesent elementum elit</li><li>At tellus nec ultricies</li><li>Sit amet porttitor</li><li>Mattis enim in massa</li><li>Libero interdum nec</li></ul>
    <p class="price">$ 85.99</p>
  </div>
</section>

<section class="recipes">
  <h2 class="center-title" style="top:38px">OUR RECIPES</h2>
  <article class="recipe-card" style="left:120px;top:104px;width:628px;height:546px;z-index:2">
    <div class="recipe-img" style="height:426px;background:linear-gradient(135deg,#7a9a3c,#b9402e 40%,#f1e7d6 60%,#e7a93a 75%,#6f8f35)" role="img" aria-label="Salad with boiled eggs, bacon and dressing"></div>
    <div class="recipe-body" style="top:442px">
      <h3 class="recipe-title">Meal Title here</h3>
      <p class="recipe-text">Place half of the broccoli, and cut the carrot into small pieces, roughly chop up the onion and half of the capsicum, put to one side.</p>
    </div>
  </article>
  <article class="recipe-card small" style="left:758px;top:104px;width:299px;height:270px;z-index:2">
    <div class="recipe-img" style="height:176px;background:linear-gradient(135deg,#a9744a,#d9b48a 50%,#7c4f33)" role="img" aria-label="Baked protein balls on a plate"></div>
    <div class="recipe-body" style="top:188px">
      <h3 class="recipe-title">Meal Title here</h3>
      <p class="recipe-text">The Golden Wok take on this delicious favourite using Golden Wok Laksa Paste.</p>
    </div>
  </article>
  <article class="recipe-card small" style="left:758px;top:384px;width:299px;height:263px;z-index:2">
    <div class="recipe-img" style="height:162px;background:linear-gradient(135deg,#e6dccb,#f08a2e 50%,#d9c9a8)" role="img" aria-label="Carrot sticks with a dip"></div>
    <div class="recipe-body" style="top:174px">
      <h3 class="recipe-title">Meal Title here</h3>
      <p class="recipe-text">The Golden Wok take on this delicious favourite using Golden Wok Laksa Paste.</p>
    </div>
  </article>
  <svg class="drip" style="top:620px;height:121px" viewBox="0 0 1200 121" preserveAspectRatio="none">
    <path fill="#ffffff" d="M0 121 V70 C40 50 55 100 95 92 C135 84 125 40 170 44 C210 48 205 96 245 92 C285 88 275 52 315 54 C355 56 350 90 390 86 C430 82 420 36 465 40 C505 44 500 100 540 96 C580 92 570 56 610 58 C650 60 645 88 685 84 C725 80 715 34 760 38 C800 42 795 94 835 90 C875 86 865 50 905 52 C945 54 940 96 980 92 C1020 88 1010 40 1055 42 C1095 44 1090 82 1130 78 C1165 74 1180 30 1200 22 V121 Z"/>
  </svg>
</section>

<section class="gallery">
  <h2 class="center-title" style="top:48px">PHOTO GALLERY</h2>
  <div class="tile" style="left:120px;top:117px;height:163px;background:linear-gradient(135deg,#6f8f4a,#a6b98a)" role="img" aria-label="Coach outdoors in the park"></div>
  <div class="tile" style="left:120px;top:293px;height:195px;background:linear-gradient(135deg,#4a5a78,#9aa4b6)" role="img" aria-label="Coach lifting weights in a gym"></div>
  <div class="tile" style="left:120px;top:501px;height:140px;background:linear-gradient(135deg,#8b6f5a,#c8ab92)" role="img" aria-label="Coach with her child"></div>
  <div class="tile" style="left:365px;top:117px;height:202px;background:linear-gradient(135deg,#5c7fa8,#b4c6d8)" role="img" aria-label="Coach with a friend wearing caps"></div>
  <div class="tile" style="left:365px;top:332px;height:309px;background:linear-gradient(135deg,#3b3b3b,#d9577f 55%,#7d6a5a)" role="img" aria-label="Coach with a friend in training gear"></div>
  <div class="tile" style="left:611px;top:117px;height:147px;background:linear-gradient(135deg,#3e4d7a,#c24a4a)" role="img" aria-label="Group of people at a training session"></div>
  <div class="tile" style="left:611px;top:277px;height:211px;background:linear-gradient(135deg,#2d2d2d,#e68a1f 45%,#f0a23a 60%,#2d2d2d)" role="img" aria-label="Bowl of pumpkin soup"></div>
  <div class="tile" style="left:611px;top:501px;height:140px;background:linear-gradient(135deg,#7b6552,#c9b09a)" role="img" aria-label="Coach with a friend smiling"></div>
  <div class="tile" style="left:856px;top:117px;height:306px;background:linear-gradient(135deg,#a88a72,#e0cbb6)" role="img" aria-label="Coach smiling in a cap"></div>
  <div class="tile" style="left:856px;top:436px;height:205px;background:linear-gradient(180deg,#c8d6e3,#7f8f6a 55%,#6b6b6b)" role="img" aria-label="Runner on a country road"></div>
</section>

<footer class="site-footer">
  <div class="brand">
    <span class="brand-dot"></span>
    <span class="brand-name">Kit Darvell</span>
  </div>
  <div class="footer-col" style="left:488px">
    <h3>QUICK LINKS</h3>
    <ul><li>HOME</li><li>BLOG</li><li>ABOUT</li><li>TRAINING PROGRAMS</li></ul>
  </div>
  <div class="footer-col" style="left:712px">
    <h3>SUBLINKS</h3>
    <ul><li>HEALTHY FOOD</li><li>SUBSCRIBE</li><li>TESTIMONIALS</li></ul>
  </div>
  <div class="footer-col" style="left:940px">
    <h3>SOCIAL</h3>
    <ul>
      <li class="social"><span class="dot-icon"></span>CHATWALL</li>
      <li class="social"><span class="dot-icon"></span>SNAPLOOMER</li>
      <li class="social"><span class="dot-icon"></span>VID REEL</li>
    </ul>
  </div>
  <div class="footer-rule"></div>
  <p class="copyright">© 2018 Company Name. All right reserved</p>
</footer>

</body>
</html>
```